Visitenkarten-Design für Gesundheits- und Ernährungsberaterin
Zielgruppe
Ich bin Gesundheit und Ernährungsberaterin
Zielgruppe sind chronisch Kranke und Gesundheitsbewusste Personen
Aufgabenstellung
Schlichtes aber direkt erkennbares Design.
Mahl mit Maß , Gesundheit und Ernährungsberatung ( gut lesbar , elegant)
Marlene Obruk-Feistinger ( nicht so groß )
Grau ; Grün Töne und gerne etwas rosa
Infos wie Adresse und E-Mail vielleicht in jeweilige Blöcke am unteren Rand

```html
<!DOCTYPE html>
<html lang="de">
<head>
<meta charset="utf-8">
<title>Visitenkarte – Mahl mit Maß</title>
<link href="https://fonts.googleapis.com/css2?family=Arimo:wght@400&display=swap" rel="stylesheet">
<style>
  :root {
    --page-bg: #4a4a4b;
    --panel-green: #7d9a84;
    --ribbon-pink: #d98a9c;
    --ribbon-fold: #b0687a;
    --ink-light: #ffffff;
    --photo-light: #f1f1f3;
    --photo-mid: #e2e2e6;
  }
  html, body {
    margin: 0;
    width: 1200px;
    height: 1200px;
    overflow: hidden;
    background: var(--page-bg);
    font-family: "Arimo", Arial, sans-serif;
  }
  .business-card {
    position: absolute;
    left: 50px;
    top: 294px;
    width: 1100px;
    height: 611px;
    background: var(--panel-green);
  }
  .card-photo {
    position: absolute;
    left: 0;
    top: 0;
    width: 623px;
    height: 611px;
    background: linear-gradient(160deg, var(--photo-light) 0%, var(--photo-mid) 55%, #f0c9a8 78%, var(--photo-light) 100%);
  }
  .brand-title {
    position: absolute;
    left: 639px;
    top: 26px;
    margin: 0;
    font-size: 34px;
    font-weight: 400;
    letter-spacing: 1px;
    color: var(--ink-light);
    white-space: nowrap;
  }
  .name-ribbon {
    position: absolute;
    left: 600px;
    top: 89px;
    width: 500px;
    height: 84px;
    background: var(--ribbon-pink);
  }
  .ribbon-fold {
    position: absolute;
    left: 600px;
    top: 173px;
  }
  .person-name {
    position: absolute;
    left: 639px;
    top: 98px;
    margin: 0;
    font-size: 30px;
    font-weight: 400;
    color: var(--ink-light);
    white-space: nowrap;
  }
  .person-role {
    position: absolute;
    left: 639px;
    top: 136px;
    margin: 0;
    font-size: 20px;
    color: var(--ink-light);
    white-space: nowrap;
  }
  .contact-icons {
    position: absolute;
    left: 652px;
    top: 266px;
  }
  .contact-list {
    position: absolute;
    left: 734px;
    top: 0;
    margin: 0;
    padding: 0;
    list-style: none;
    color: var(--ink-light);
    font-size: 26px;
    line-height: 31px;
  }
  .contact-list li { position: absolute; left: 0; white-space: nowrap; }
  .contact-address { top: 268px; }
  .contact-phone { top: 341px; }
  .contact-mobile { top: 384px; }
  .contact-mail { top: 428px; }
</style>
</head>
<body>
  <div class="business-card">
    <div class="card-photo" role="img" aria-label="Foto: Beraterin im weißen Kittel mit Stethoskop hält frisches Obst und Gemüse"></div>

    <h2 class="brand-title">Mahl mit Maß</h2>

    <div class="name-ribbon"></div>
    <svg class="ribbon-fold" width="23" height="23" viewBox="0 0 23 23" aria-hidden="true">
      <polygon points="0,0 23,0 23,23" fill="var(--ribbon-fold)"/>
    </svg>
    <h1 class="person-name">Marlene Obruk-Feistinger</h1>
    <p class="person-role">Gesundheit und Ernährungsberaterin</p>

    <svg class="contact-icons" width="60" height="213" viewBox="0 0 60 213" aria-hidden="true">
      <rect x="3" y="3" width="54" height="207" rx="14" fill="none" stroke="#fff" stroke-width="5"/>
      <path d="M30 19 a9 9 0 0 1 9 9 c0 7 -9 17 -9 17 s-9 -10 -9 -17 a9 9 0 0 1 9 -9z" fill="#fff"/>
      <circle cx="30" cy="28" r="3.5" fill="var(--panel-green)"/>
      <path d="M22 77 c2 -2 4 -2 5 0 l3 4 c1 2 0 3 -2 4 c1 3 4 6 7 7 c1 -2 2 -3 4 -2 l4 3 c2 1 2 3 0 5 c-2 2 -5 3 -9 1 c-6 -3 -11 -8 -13 -14 c-1 -4 0 -6 1 -8z" fill="#fff"/>
      <rect x="24" y="120" width="13" height="23" rx="2" fill="none" stroke="#fff" stroke-width="2.5"/>
      <circle cx="30.5" cy="139" r="1.5" fill="#fff"/>
      <rect x="18" y="171" width="25" height="16" fill="#fff"/>
      <polyline points="18,171 30.5,181 43,171" fill="none" stroke="var(--panel-green)" stroke-width="2"/>
      <path d="M18 187 L27 179 M43 187 L34 179" fill="none" stroke="var(--panel-green)" stroke-width="1.5"/>
    </svg>

    <ul class="contact-list">
      <li class="contact-address">Lindenkamp 7,<br>24795 Wiesenrode</li>
      <li class="contact-phone">04352/7720416</li>
      <li class="contact-mobile">0152/38804517</li>
      <li class="contact-mail">ernaehrung-mof@postfeld.de</li>
    </ul>
  </div>
</body>
</html>
```